"Kolvarisk" Show on Strovana and plavento needs a thumbnail.

Hello, I need a thumbnail image for a new show I want to start Strovana and Plavento soon. This show represents different styles of music out of all EDM genres mixed to approx. one hour sets. Please find attached CD covers I really like in their style and which can be used as inspiration. This show should be released on a weekly basis. So I want to attach my logo which needs to be thumbnailed / image as well

Target Market(s)

Young EDM Lovers

Industry/Entity Type

Plavento

Requirements
Must have
• The cover needs to have the above mentioned title in a cool lettering and the name of the artist (which can be found in the attached pictures in color and style. should represent electronic music.
Nice to have
• I imagine child of earth ball instead of speakers or symbols in the cover. It shall represent the (re-) union which happens when young people come together and share their passion for music. Does not matter which style it is. It's also nice to have a space for adding social media information on the thumbnail.
Should not have
• Should not be too colorful. No comic style.

```html
<!DOCTYPE html>
<html lang="en">
<head>
<meta charset="utf-8">
<title>Kolvarisk – Chapter 1</title>
<link rel="stylesheet" href="https://fonts.googleapis.com/css2?family=Montserrat:wght@800&family=Russo+One&family=Cormorant+Garamond:ital,wght@1,500&display=swap">
<style>
  :root {
    --bg-top: #2a1238;
    --bg-mid: #3d1a5a;
    --bg-deep: #07040a;
    --panel: #ffffff;
    --ink: #12121a;
    --light: #f4f0f8;
    --brand-blue: #1f7fd0;
    --glow-pink: #ff4f8a;
  }
  html, body {
    margin: 0;
    padding: 0;
    width: 1200px;
    height: 1173px;
    overflow: hidden;
    background: var(--bg-deep);
  }
  .cover {
    position: relative;
    width: 1200px;
    height: 1173px;
    overflow: hidden;
    background:
      radial-gradient(ellipse 70% 55% at 50% 42%, var(--bg-mid) 0%, var(--bg-top) 60%, #1a0b24 85%),
      var(--bg-top);
  }
  .cover::after {
    content: "";
    position: absolute;
    left: 0; right: 0; bottom: 0;
    height: 320px;
    background: linear-gradient(to bottom, rgba(7,4,10,0) 0%, var(--bg-deep) 80%);
    pointer-events: none;
  }
  .artwork {
    position: absolute;
    inset: 0;
    width: 1200px;
    height: 1173px;
  }
  .speakers {
    position: absolute;
    inset: 0;
    width: 1200px;
    height: 1173px;
    z-index: 2;
  }
  .brand {
    position: absolute;
    top: 84px;
    left: 0;
    width: 1200px;
    text-align: center;
    font-family: "Russo One", sans-serif;
    font-size: 40px;
    letter-spacing: 3px;
    color: var(--brand-blue);
    line-height: 48px;
  }
  .title-panel {
    position: absolute;
    left: 161px;
    top: 482px;
    width: 871px;
    height: 167px;
    background: var(--panel);
    display: flex;
    align-items: center;
    justify-content: center;
  }
  .title {
    margin: 0;
    font-family: "Montserrat", sans-serif;
    font-weight: 800;
    font-size: 100px;
    letter-spacing: -4px;
    color: var(--ink);
  }
  .chapter {
    position: absolute;
    left: 572px;
    top: 802px;
    font-family: "Russo One", sans-serif;
    font-size: 30px;
    color: var(--light);
    transform: rotate(-30deg);
    transform-origin: left bottom;
    white-space: nowrap;
  }
  .guest {
    position: absolute;
    right: 62px;
    top: 740px;
    text-align: right;
    font-family: "Cormorant Garamond", serif;
    font-style: italic;
    font-weight: 500;
    font-size: 33px;
    line-height: 34px;
    color: var(--light);
  }
  .guest p { margin: 0; }
  .guest .indent-1 { margin-right: -2px; }
  .guest .indent-2 { margin-right: 12px; }
  .social {
    position: absolute;
    left: 984px;
    top: 1052px;
    z-index: 3;
    font-family: "Cormorant Garamond", serif;
    font-style: italic;
    font-weight: 500;
    font-size: 29px;
    color: var(--light);
  }
  .social-row {
    display: flex;
    align-items: center;
    gap: 10px;
    height: 40px;
  }
  .social-mark {
    width: 24px;
    height: 24px;
    background: var(--light);
    flex: none;
  }
  .social-mark.round { border-radius: 50%; }
</style>
</head>
<body>
<main class="cover">
  <svg class="artwork" viewBox="0 0 1289 1260" preserveAspectRatio="none" aria-hidden="false">
    <defs>
      <linearGradient id="strip-gold" x1="0" y1="1" x2="1" y2="0">
        <stop offset="0" stop-color="#b9c6a8"/>
        <stop offset="0.5" stop-color="#b69a3e"/>
        <stop offset="1" stop-color="#6f7a45"/>
      </linearGradient>
      <linearGradient id="strip-red" x1="0" y1="1" x2="1" y2="0">
        <stop offset="0" stop-color="#6b1a22"/>
        <stop offset="0.45" stop-color="#c2303a"/>
        <stop offset="1" stop-color="#f07aa0"/>
      </linearGradient>
      <linearGradient id="strip-blue" x1="0" y1="1" x2="1" y2="0">
        <stop offset="0" stop-color="#3a2c6e"/>
        <stop offset="0.5" stop-color="#6a4aa8"/>
        <stop offset="1" stop-color="#4a58b8"/>
      </linearGradient>
      <radialGradient id="glow" cx="0.5" cy="0.5" r="0.5">
        <stop offset="0" stop-color="#ffffff"/>
        <stop offset="0.3" stop-color="#ff6a9a"/>
        <stop offset="1" stop-color="#ff4f8a" stop-opacity="0"/>
      </radialGradient>
    </defs>
    <rect class="side-glow" x="1110" y="300" width="180" height="260" fill="#a0244e" opacity="0.35" transform="rotate(12 1200 430)"/>
    <g class="photo-strips">
      <polygon role="img" aria-label="Festival photo: fireworks over a crowd in gold light" points="220,680 680,323 760,470 255,757" fill="url(#strip-gold)"/>
      <polygon role="img" aria-label="Festival photo: crowd under red and pink stage lights" points="375,700 865,393 940,520 440,825" fill="url(#strip-red)"/>
      <polygon role="img" aria-label="Festival photo: laser show over a stage in blue and violet" points="520,745 1025,490 1080,640 575,885" fill="url(#strip-blue)"/>
    </g>
    <g class="light-flares">
      <ellipse cx="640" cy="348" rx="70" ry="8" fill="url(#glow)"/>
      <ellipse cx="835" cy="843" rx="70" ry="8" fill="url(#glow)"/>
      <ellipse cx="1115" cy="730" rx="10" ry="40" fill="url(#glow)"/>
    </g>
  </svg>

  <div class="brand">VELTRANO</div>

  <div class="title-panel">
    <h1 class="title">KOLVARISK</h1>
  </div>

  <div class="chapter">CHAPTER 1</div>

  <div class="guest">
    <p>Guest Dj:</p>
    <p class="indent-1">Marek Solvane</p>
    <p class="indent-2">@mareksolvane</p>
    <p>Top Global Dj</p>
  </div>

  <svg class="speakers" viewBox="0 0 1289 1260" preserveAspectRatio="none">
    <defs>
      <radialGradient id="cone" cx="0.5" cy="0.4" r="0.6">
        <stop offset="0" stop-color="#5a5a60"/>
        <stop offset="0.5" stop-color="#1e1e22"/>
        <stop offset="1" stop-color="#050506"/>
      </radialGradient>
    </defs>
    <g role="img" aria-label="Row of loudspeakers at the bottom of the cover">
      <circle cx="485" cy="1275" r="95" fill="url(#cone)"/>
      <circle cx="820" cy="1275" r="90" fill="url(#cone)"/>
      <circle cx="652" cy="1265" r="115" fill="url(#cone)"/>
    </g>
  </svg>

  <div class="social">
    <div class="social-row"><span class="social-mark round"></span>@sample</div>
    <div class="social-row"><span class="social-mark"></span>kolvarisk</div>
  </div>
</main>
</body>
</html>
```